Design an App Mockup for a Gym

Hi, I just need the design of the app, I need the files in Illustrator (.ai ) or Photoshop. So I can modify things later.

design 1- Home (Welcome/log in/sign up)
2- Register your name, age, weight,height,id number, gender
3-confirmation window and message to check email to verify your account
4-Your profile and 3 options to choose if you want to loose weight, fit, build muscle.
5- Calendar with different routines everyday
6-View your progress of the week

you can add more windows if you want , create new things. The design should be attractive, modern, and cool. The target market is students.

I will attach a very basic sketch

I will choose the winner of the contest tonight, I need it before 4am (-6)

```html
<!DOCTYPE html>
<html lang="es">
<head>
<meta charset="utf-8">
<title>Nexo Gym – Verifique su cuenta</title>
<link rel="stylesheet" href="https://fonts.googleapis.com/css2?family=Open+Sans:wght@400;700&family=Pacifico&family=Montserrat:wght@800&display=swap">
<style>
  :root {
    --stage: #5e5e5e;
    --screen: #f2f2f2;
    --header: #3a3a3c;
    --title-blue: #1aa7e0;
    --ink: #1a1a1a;
    --field: #e6e7e9;
    --link-green: #8dc63f;
    --accent-orange: #fbb040;
    --accent-orange-dark: #f39a2b;
    --white: #ffffff;
  }
  * { box-sizing: border-box; margin: 0; padding: 0; }
  html, body {
    width: 1200px; height: 1125px; overflow: hidden;
    background: var(--stage);
  }
  .app-screen {
    position: absolute; left: 321px; top: 91px;
    width: 547px; height: 937px;
    background: var(--screen);
    border: 1px solid #111;
    font-family: "Open Sans", sans-serif;
    color: var(--ink);
  }
  .app-header {
    position: absolute; left: 0; top: 0; width: 100%; height: 135px;
  }
  .app-header svg { position: absolute; left: 0; top: 0; }
  .brand {
    position: absolute; left: 43px; top: 20px; height: 70px;
    display: flex; align-items: center; gap: 18px;
  }
  .brand-dot {
    width: 62px; height: 62px; border-radius: 50%;
    background: var(--link-green);
  }
  .brand-name {
    font-family: "Open Sans", sans-serif; font-weight: 700;
    font-size: 52px; letter-spacing: 1px; color: var(--white);
  }
  .screen-title {
    position: absolute; left: 34px; top: 168px;
    font-family: "Pacifico", cursive; font-weight: 400;
    font-size: 50px; color: var(--title-blue); line-height: 1.4;
  }
  .screen-message {
    position: absolute; left: 34px; top: 290px; width: 480px;
    font-size: 23.5px; line-height: 30.5px;
  }
  .email-field {
    position: absolute; left: 34px; top: 581px;
    width: 480px; height: 47px;
    background: var(--field); border-radius: 5px;
  }
  .change-address {
    position: absolute; left: 34px; top: 643px;
    font-size: 30px; color: var(--link-green); line-height: 1.4;
  }
  .done-button {
    position: absolute; left: 175px; top: 754px;
    width: 197px; height: 82px;
    background: var(--accent-orange);
    border-radius: 12px;
    box-shadow: inset 0 -5px 0 var(--accent-orange-dark);
    font-family: "Montserrat", sans-serif; font-weight: 800;
    font-size: 38px; color: var(--white);
    display: flex; align-items: center; justify-content: center;
    padding-bottom: 4px;
  }
</style>
</head>
<body>
  <main class="app-screen">
    <header class="app-header">
      <svg width="547" height="135" viewBox="0 0 547 135">
        <path fill="var(--header)" d="M0 0 H547 V118
          q-9 8 -18 0 q-9 -8 -18 0 q-9 8 -18 0 q-9 -8 -18 0 q-9 8 -18 0 q-9 -8 -18 0
          q-9 8 -18 0 q-9 -8 -18 0 q-9 8 -18 0 q-9 -8 -18 0 q-9 8 -18 0 q-9 -8 -18 0
          q-9 8 -18 0 q-9 -8 -18 0 q-9 8 -18 0 q-9 -8 -18 0 q-9 8 -18 0 q-9 -8 -18 0
          q-9 8 -18 0 q-9 -8 -18 0 q-9 8 -18 0 q-9 -8 -18 0 q-9 8 -18 0 q-9 -8 -18 0
          q-9 8 -18 0 q-9 -8 -18 0 q-9 8 -18 0 q-9 -8 -18 0 q-9 8 -18 0 q-9 -8 -18 0
          q-5 5 -7 2 V0 Z"/>
      </svg>
      <div class="brand">
        <span class="brand-dot"></span>
        <span class="brand-name">NEXO GYM</span>
      </div>
    </header>

    <h1 class="screen-title">Verifiquesu cuenta</h1>

    <p class="screen-message">Un correo electrónico ha sido enviado a la siguiente dirección con un enlace para verificar su cuenta Nexo. Asegúrese de revisar su correo electrónico y siga el enlace para completar la creación de su cuenta de Nexo.</p>

    <div class="email-field"></div>
    <p class="change-address">Dirección de cambio</p>

    <div class="done-button">HECHO</div>
  </main>
</body>
</html>
```